Business Card Design for Clinical Therapist

I will operate in 3 product areas as follows...
I will operate as Psychotherapist providing an opportunity for individuals to stop, reflect, heal, and gain hope in a safe and professional atmosphere. My task as a Licensed Mental Health Social Worker is to work “along-side” the client to help guide them toward answers they may seek. I believe that all difficulties contain a small seed of opportunity within them and I can support the individual in clarifying issues while resolving obstacles that may get in the way.
1-Therapy
Treatment Issues may include:
• Addiction
• Bipolar Disorder
• Adolescent or Adult
• Coping Skills
• Dual Diagnosis
• Family Conflict
• Sleep or Insomnia
• Substance Abuse
• Anger Management
• Career Counseling
• Drug Abuse
• Emotional Disturbance
• Grief
• Self Esteem
• Trauma and PTSD
Treatment Orientation may include but not be limited to:
• CBT
• EMDR
• Person-Centered
• Mindfulness based (MBCT)
• Motivational Interviewing

2-Other Substance Abuse Services
SAP Assessments
Employees performing safety-sensitive duties under US Bureau of Roadway Affairs rules must have an evaluation by a qualified Substance Abuse Professional when they are in violation of BRA rules (for a positive test or a refusal to test). I am a BRA qualified SAP and can perform these evaluations, which involve specialized assessment and compliance reports, as well as a return to work assessment.

3-DUI/OVUII Assessments
Substance abuse assessment reports-State level assessments targeted for the court system.

Somehow I would like the final design to acknowledge the three areas of services, or two being therapy for mental health services and combining SAP/OVUII assessment reporting for Substance abuse)

Industry/Entity Type

Mental Health

Contact Information for Business Card

Brightwell Harbor LLC,
Desmond Farrowby LCSW
Clinical Therapist
2087 West Palmer Avenue, STE 412
Honolulu, HI 96720
808.555.0193
brightwellharborllc.example

Colors

Designer to choose colors to be used in the design.

```html
<!DOCTYPE html>
<html lang="en">
<head>
<meta charset="utf-8">
<title>Brightwell Harbor LLC — Business Card</title>
<link rel="stylesheet" href="https://fonts.googleapis.com/css2?family=Lato:wght@400;700&family=Lora:wght@700&display=swap">
<style>
  :root{
    --bg:#e8e3da;
    --blue-deep:#0a5fae;
    --blue-mid:#1686cc;
    --blue-light:#26b0dc;
    --orange:#f0a030;
    --purple:#4a44b8;
    --ink-purple:#5550c0;
    --white:#ffffff;
    --paper:#f6f6f6;
  }
  *{margin:0;padding:0;box-sizing:border-box}
  html,body{width:1200px;height:1023px;overflow:hidden}
  body{background:var(--bg);font-family:"Lato",Arial,sans-serif;position:relative}
  .card{position:absolute;width:700px;height:400px;border-radius:4px;overflow:hidden;
        box-shadow:0 6px 18px rgba(0,0,0,.18)}
  .card svg.card-art{position:absolute;inset:0;width:100%;height:100%}
  .card-front{left:250px;top:60px}
  .card-back{left:250px;top:560px}

  .company-name{position:absolute;left:60px;top:236px;color:var(--white);
        font-family:"Lora",Georgia,serif;font-weight:700;font-size:19px}

  .identity{position:absolute;right:50px;top:58px;text-align:right}
  .person-name{color:var(--ink-purple);font-weight:700;font-size:27px;letter-spacing:.2px}
  .person-title{color:var(--orange);font-size:18px;margin-top:4px}

  .contact{position:absolute;right:50px;top:172px;list-style:none;color:var(--ink-purple);font-size:16px}
  .contact li{display:flex;justify-content:flex-end;align-items:flex-start;gap:12px;margin-bottom:16px;text-align:right;line-height:1.3}
  .contact .icon{flex:0 0 22px;width:22px;height:22px;background:var(--orange);border-radius:2px;display:flex;align-items:center;justify-content:center;margin-top:0}
  .contact .icon svg{width:14px;height:14px}

  .issues,.orientation{position:absolute;list-style:none;color:var(--white);font-size:14.5px;line-height:21px}
  .issues{left:44px;top:40px}
  .orientation{left:320px;top:196px}
  .issues li::before,.orientation li::before{content:"";display:inline-block;width:5px;height:5px;background:var(--white);border-radius:50%;margin-right:9px;vertical-align:middle}
  .divider{position:absolute;left:320px;top:150px;width:150px;height:3px;background:var(--white)}
</style>
</head>
<body>

<section class="card card-front" aria-label="Business card front">
  <svg class="card-art" viewBox="0 0 700 400" preserveAspectRatio="none" aria-hidden="true">
    <defs>
      <linearGradient id="frontBlue" x1="0" y1="0" x2="1" y2="1">
        <stop offset="0" stop-color="#0a5fae"/>
        <stop offset=".6" stop-color="#1686cc"/>
        <stop offset="1" stop-color="#26b0dc"/>
      </linearGradient>
    </defs>
    <rect width="700" height="400" fill="url(#frontBlue)"/>
    <path d="M228,0 C255,190 350,330 440,400 L700,400 L700,0 Z" fill="var(--orange)"/>
    <path d="M258,0 C275,95 300,180 335,230 C370,300 410,360 465,400 L700,400 L700,0 Z" fill="var(--purple)"/>
    <path d="M262,0 C285,175 375,325 505,400 L700,400 L700,0 Z" fill="var(--paper)"/>
  </svg>

  <p class="company-name">Brightwell Harbor LLC</p>

  <div class="identity">
    <h1 class="person-name">Desmond Farrowby</h1>
    <p class="person-title">LCSW Clinical Therapist</p>
  </div>

  <ul class="contact">
    <li><span>808.555.0193</span>
      <span class="icon"><svg viewBox="0 0 14 14"><rect x="4" y="1" width="6" height="12" rx="1" fill="none" stroke="#fff" stroke-width="1.4"/></svg></span></li>
    <li><span>brightwellharborllc.example</span>
      <span class="icon"><svg viewBox="0 0 14 14"><circle cx="7" cy="7" r="5.5" fill="none" stroke="#fff" stroke-width="1.4"/><circle cx="7" cy="7" r="2" fill="none" stroke="#fff" stroke-width="1.4"/></svg></span></li>
    <li><span>2087 West Palmer Avenue,<br>STE 412 Honolulu, HI 96720</span>
      <span class="icon"><svg viewBox="0 0 14 14"><path d="M2,7 L7,2 L12,7 M3.5,6 V12 H10.5 V6" fill="none" stroke="#fff" stroke-width="1.4"/></svg></span></li>
  </ul>
</section>

<section class="card card-back" aria-label="Business card back">
  <svg class="card-art" viewBox="0 0 700 400" preserveAspectRatio="none" aria-hidden="true">
    <defs>
      <linearGradient id="backBlue" x1="0" y1="0" x2="1" y2="1">
        <stop offset="0" stop-color="#0a5fae"/>
        <stop offset=".5" stop-color="#1686cc"/>
        <stop offset="1" stop-color="#0a5fae"/>
      </linearGradient>
    </defs>
    <rect width="700" height="400" fill="url(#backBlue)"/>
    <path d="M440,400 C470,300 560,240 700,215 L700,400 Z" fill="var(--orange)"/>
    <path d="M478,400 C505,305 585,255 700,240 L700,400 Z" fill="var(--paper)"/>
  </svg>

  <ul class="issues">
    <li>Addiction</li><li>Bipolar Disorder</li><li>Adolescent or Adult</li><li>Coping Skills</li>
    <li>Dual Diagnosis</li><li>Family Conflict</li><li>Sleep or Insomnia</li><li>Substance Abuse</li>
    <li>Anger Management</li><li>Career Counseling</li><li>Drug Abuse</li><li>Emotional Disturbance</li>
    <li>Grief</li><li>Self Esteem</li><li>Trauma and PTSD</li>
  </ul>

  <div class="divider"></div>

  <ul class="orientation">
    <li>CBT</li><li>EMDR</li><li>Person-Centered</li><li>Mindfulness based (MBCT)</li><li>Motivational Interviewing</li>
  </ul>
</section>

</body>
</html>
```